I need a box design created for a DNA Fitness Test

I need a modern and sleek box design for a fitness test. The box needs to have our logo on it and should be clean and modern. The Box is 9 Inches Long 3 and 3/4 inches wide, and 2 inches tall. Company logo attached. The company name is cedar vitality.

Target Market(s)

Fitness

Industry/Entity Type

Fitness

Requirements
Must have
• Our logo

```html
<!DOCTYPE html>
<html lang="en">
<head>
<meta charset="utf-8">
<title>Cedar Vitality – DNA Fitness Test Box Dieline</title>
<link href="https://fonts.googleapis.com/css2?family=Montserrat:wght@400;600;800&family=Open+Sans:wght@400;600&display=swap" rel="stylesheet">
<style>
  :root {
    --backdrop: #8c8d8f;
    --board: #ffffff;
    --fold: #e3e4e6;
    --navy: #1d2a44;
    --accent-blue: #2a7fc9;
    --accent-green: #7cc242;
    --body-text: #5b6270;
  }
  html, body {
    margin: 0;
    width: 1200px;
    height: 2668px;
    overflow: hidden;
    background: var(--backdrop);
  }
  .dieline {
    position: absolute;
    left: 0;
    top: 754px;
    width: 1200px;
    height: 1160px;
  }
  .panel {
    position: absolute;
    background: var(--board);
    box-shadow: inset 0 0 0 1px var(--fold);
    box-sizing: border-box;
  }
  .panel--lid    { left: 200px; top: 0;     width: 800px;  height: 260px; }
  .panel--end-l  { left: 0;     top: 260px; width: 200px;  height: 420px; }
  .panel--front  { left: 200px; top: 260px; width: 800px;  height: 420px; }
  .panel--end-r  { left: 1000px;top: 260px; width: 200px;  height: 420px; }
  .panel--base   { left: 200px; top: 680px; width: 800px;  height: 480px; }

  .brand {
    display: flex;
    align-items: center;
    gap: 14px;
    position: absolute;
  }
  .brand__dot {
    width: 34px;
    height: 34px;
    border-radius: 50%;
    background: var(--accent-green);
    flex: none;
  }
  .brand__name {
    font-family: "Montserrat", sans-serif;
    font-weight: 800;
    font-size: 30px;
    letter-spacing: 1px;
    color: var(--navy);
    text-transform: uppercase;
    white-space: nowrap;
  }
  .panel--lid .brand   { left: 40px; top: 150px; }
  .panel--base .brand  { left: 40px; top: 50px; }
  .panel--front .brand { right: 40px; top: 180px; }
  .panel--end-l .brand {
    left: 50%;
    top: 50%;
    transform: translate(-50%, -50%) rotate(-90deg);
  }
  .panel--end-l .brand__name { font-size: 24px; }
  .panel--end-l .brand__dot { width: 26px; height: 26px; }

  .front-copy {
    position: absolute;
    left: 40px;
    top: 44px;
    width: 420px;
    font-family: "Open Sans", sans-serif;
    color: var(--body-text);
  }
  .front-copy__title {
    margin: 0 0 20px;
    font-family: "Montserrat", sans-serif;
    font-weight: 600;
    font-size: 28px;
    letter-spacing: 1px;
    color: var(--accent-blue);
  }
  .front-copy__intro {
    margin: 0 0 18px;
    font-size: 13px;
    line-height: 1.55;
  }
  .front-copy__list {
    margin: 0 0 18px;
    padding-left: 18px;
    font-size: 13px;
    line-height: 1.6;
  }
  .front-copy__sign {
    margin: 0;
    font-size: 13px;
  }

  .helix-art {
    position: absolute;
    right: 40px;
    top: 60px;
    width: 300px;
    height: 380px;
    border-radius: 150px;
    background: linear-gradient(200deg, #cfe9b0 0%, #8fcf5a 50%, #e6f3d8 100%);
    opacity: 0.85;
  }
</style>
</head>
<body>
  <main class="dieline">
    <section class="panel panel--lid">
      <div class="brand"><span class="brand__dot"></span><span class="brand__name">Cedar Vitality</span></div>
    </section>

    <section class="panel panel--end-l">
      <div class="brand"><span class="brand__dot"></span><span class="brand__name">Cedar Vitality</span></div>
    </section>

    <section class="panel panel--front">
      <div class="front-copy">
        <h1 class="front-copy__title">UNLOCK YOUR POTENTIAL</h1>
        <p class="front-copy__intro">Our kit reads the markers that shape how your body trains, recovers and responds. Simple at home sampling, a secure lab and a clear report help you build a plan that is truly yours.</p>
        <ul class="front-copy__list">
          <li>Saliva collection swab</li>
          <li>Prepaid return envelope</li>
          <li>Activation card</li>
          <li>Step by step guide</li>
          <li>Secure results access</li>
        </ul>
        <p class="front-copy__sign">Get fit for life with Cedar Vitality.</p>
      </div>
      <div class="brand"><span class="brand__dot"></span><span class="brand__name">Cedar Vitality</span></div>
    </section>

    <section class="panel panel--end-r"></section>

    <section class="panel panel--base">
      <div class="brand"><span class="brand__dot"></span><span class="brand__name">Cedar Vitality</span></div>
      <div class="helix-art" role="img" aria-label="Green DNA double helix illustration"></div>
    </section>
  </main>
</body>
</html>
```